Business Cards

Business card design for my company.
I would like the card's background colour to be black. You can also see our web site to get an idea of our brand. https://www.dlqmarrowfield.com.au/
- Name
- Email

```html
<!DOCTYPE html>
<html lang="en">
<head>
<meta charset="utf-8">
<title>DLQ Marrowfield — Business Cards</title>
<link href="https://fonts.googleapis.com/css2?family=Open+Sans:wght@400;600;700&display=swap" rel="stylesheet">
<style>
  :root {
    --backdrop: #2b2b2c;
    --card: #1b1b1c;
    --band-dark: #111112;
    --band-light: #4a4a4c;
    --green: #109a3c;
    --white: #f4f4f4;
    --muted: #d8d8d8;
    --rule: #8a8a8a;
  }
  * { margin: 0; padding: 0; box-sizing: border-box; }
  html, body { width: 1200px; height: 1088px; overflow: hidden; }
  body {
    background: var(--backdrop);
    font-family: "Open Sans", Arial, sans-serif;
    display: flex;
    flex-direction: column;
    align-items: center;
    justify-content: center;
    gap: 64px;
  }
  .card {
    position: relative;
    width: 700px;
    height: 428px;
    background: var(--card);
    border-radius: 4px;
    overflow: hidden;
    box-shadow: 0 18px 40px rgba(0,0,0,0.45);
  }
  .brand {
    display: flex;
    align-items: center;
    gap: 14px;
    color: var(--white);
    font-weight: 700;
    letter-spacing: 0.04em;
    text-transform: uppercase;
    white-space: nowrap;
  }
  .brand-square { background: var(--green); flex: none; }

  /* Front */
  .card-front .brand {
    position: absolute;
    left: 58px;
    top: 196px;
    font-size: 27px;
  }
  .card-front .brand-square { width: 18px; height: 18px; }
  .divider {
    position: absolute;
    left: 374px;
    top: 92px;
    width: 1px;
    height: 244px;
    background: var(--rule);
  }
  .details {
    position: absolute;
    left: 400px;
    top: 102px;
    color: var(--muted);
    font-size: 15.5px;
    line-height: 1.4;
  }
  .details .name {
    color: var(--green);
    font-weight: 600;
    font-size: 19px;
    letter-spacing: 0.02em;
    text-transform: uppercase;
  }
  .details .title { color: var(--white); margin-bottom: 16px; }
  .details .location { margin-bottom: 16px; }
  .contact-list { list-style: none; }
  .contact-list li { display: flex; align-items: center; gap: 8px; }
  .contact-list svg { width: 12px; height: 12px; flex: none; fill: var(--green); }

  /* Back */
  .band { position: absolute; inset: 0; }
  .card-back .brand {
    position: absolute;
    left: 50%;
    top: 50%;
    transform: translate(-50%, -50%);
    font-size: 44px;
    gap: 20px;
  }
  .card-back .brand-square { width: 28px; height: 28px; }
</style>
</head>
<body>

  <section class="card card-front" aria-label="Business card front">
    <div class="brand"><span class="brand-square"></span>DLQ Marrowfield</div>
    <div class="divider"></div>
    <div class="details">
      <p class="name">Daniel Weller</p>
      <p class="title">Managing Director</p>
      <p class="location">Hobart, Tasmania<br>Australia</p>
      <ul class="contact-list">
        <li>
          <svg viewBox="0 0 24 24" aria-hidden="true"><path d="M6.6 10.8a15.1 15.1 0 0 0 6.6 6.6l2.2-2.2c.3-.3.7-.4 1-.2 1.1.4 2.3.6 3.6.6.6 0 1 .4 1 1V20c0 .6-.4 1-1 1A17 17 0 0 1 3 4c0-.6.4-1 1-1h3.5c.6 0 1 .4 1 1 0 1.3.2 2.5.6 3.6.1.3 0 .7-.2 1z"/></svg>
          0400 555 017
        </li>
        <li>
          <svg viewBox="0 0 24 24" aria-hidden="true"><path d="M2 5h20v14H2zm2 2v.5l8 5 8-5V7l-8 5z"/></svg>
          info@dlqmarrowfield.com.au
        </li>
        <li>
          <svg viewBox="0 0 24 24" aria-hidden="true"><circle cx="12" cy="12" r="10"/></svg>
          www.dlqmarrowfield.com.au
        </li>
      </ul>
    </div>
  </section>

  <section class="card card-back" aria-label="Business card back">
    <svg class="band" viewBox="0 0 700 428" preserveAspectRatio="none" aria-hidden="true">
      <defs>
        <linearGradient id="bandShade" x1="0" y1="1" x2="1" y2="0">
          <stop offset="0" stop-color="var(--band-dark)"/>
          <stop offset="0.55" stop-color="#1f1f20"/>
          <stop offset="1" stop-color="var(--band-light)"/>
        </linearGradient>
      </defs>
      <polygon points="0,330 0,372 300,72 700,72 700,36 282,36" fill="url(#bandShade)"/>
    </svg>
    <div class="brand"><span class="brand-square"></span>DLQ Marrowfield</div>
  </section>

</body>
</html>
```